Flyer for an pediatric sleep consultancy - to distribute to play and childcare centers etc.

I need a flyer that will attract the attention of parents with children between the age of babies to toddlers, who may be experiencing sleep issues. The flyer will be placed at places such as community centers, doctors room, play centers, kindergardens, etc.

My company is called "The Quiet Meadow Studio" and provides a sleep consultancy service. My service essentially provides a customized plan for parents to follow and general advice and guidance. It is not medical advice.

I like to the flyer to have an overall tone that is soft and peaceful with a clean and beautiful design, however can catch the attention of parents who may be struggling with their child's sleep issues and are sleep deprived. I would like photos with minimal text. The colour I use is a brownish rose. I will attach some of my designs to give you an idea. You can have a look at my homepage as well to get an idea about my esthetic direction and the colour. Although the colour of my page is a bit too brownish....

I will provide the text to appear in the flyer once I have a better idea of the layout that I prefer for the flyer. The text however wont be extensive, just some catchy points.

I want to direct people to my website which is www.quietmeadowstudio-example.com
I offer a first FREE evaluation call, to the parents, to get to know each other better, learn about their child's particular sleep problems and see if we are a good fit and can work together. I would like to have this information somehow on the flyer, so that the parents will contact me.
I also have a facebook page, which is: The Quiet Meadow Studio

I have a logo that I would like to appear on the flyer. I will attach the file once the uploader on art bazaar is fixed.

When I print the flyer - I like to print A5 SIZE ... please make sure the formatting is OK for this size.

Here are some text ideas. of course all of it would be too much, I guess. On the front of the flyer I would like to have some catchy phrase or something similar to get people interested and to want to know more. On the back there could be a bit more text and information. But I'm open too suggestions....
I'm not too sure about the wording yet. But here are some text that I might be use:

Is sleep an issue in your home?

Is your baby having trouble sleeping? ... are you?!
I can help!

Sleep, baby, sleep….

Teaching children how to sleep

The Quiet Meadow Studio is a pediatric sleep consultancy that specializes in helping parents with children who struggle to develop good and healthy sleep habits.
Disruptive sleep patterns or not enough sleep can affect the physical, mental and emotional development of your child.

Of course nobody plans to have a sleep problem, but habits can become easily ingrained and spiral quickly out of control and you can find yourself sleep deprived, desperate and not too sure what to do. You see all the other sleeping babies and wish there was someone who understood what you were going through?! Well, there is!

Contact me for a free 15 minute consultation.

This 15 minute „mini“ consultation is a chance to discuss your unique sleep challenges and sleep goals with me. I will provide you with an overview of how I will work with your family to achieve your wildest sleep dreams (goals).
Furthermore do I understand and believe that every child and their family is unique and there is no one size fits all!
I would love to have a chat with you and talk about how I can help make things easier for you and your family!

Do I need a sleep consultant for my child?
The answer is yes if:
- if your child will only fall asleep when nursing or bottle feeding
- if your child needs a dummy or other external aid, like being rocked, patted or taken for a care ride to fall asleep
- if your good night routine is a challenging and exhausting procedure instead of a relaxed and enjoyable moment for the whole family
- if sleep is a constant battle in your home which leaves you feeling frustrated and exhausted
- if your own lack of sleep is taking a toll on you and the whole family

What can I do for you?

I will:

- Guide you to set an age appropriate foundation for good sleep
- Create an individual sleep plan tailored especially to your child’s sleep needs and circumstances
- Help you to teach your childto go to sleep and get back to sleep independently during the night
- show you how to teach your child to take healthful, restorative naps
-Learn

Contact:

Marta Lindqvist
info@quietmeadowstudio-example.com
www.quietmeadowstudio-example.com
+34 612 380 574

Consultations in English, German or Spanish via Phone/VidLink or home consultation

Reason: I have to go on a business trip and won't be able to choose a design until the deadline. During the trip I won't have time to give feedback and ask for changes. thank you

Target Market(s)

parents, sleep deprived mothers, young families, child care provider,

Industry/Entity Type

Baby Care

Contact Information for Business Card

Marta Lindqvist
pediatric sleep consultant
+34 612 380 574

```html
<!DOCTYPE html>
<html lang="en">
<head>
<meta charset="utf-8">
<title>The Quiet Meadow Studio – A5 Flyer</title>
<link href="https://fonts.googleapis.com/css2?family=Raleway:ital,wght@0,300;0,400;0,500;0,700;0,800;1,400;1,700&display=swap" rel="stylesheet">
<style>
  :root{
    --rose:#c98b7d;
    --rose-soft:#e7c3b8;
    --sage:#7f938d;
    --sage-line:#9fb0aa;
    --ink:#3a3a3a;
    --paper:#ffffff;
    --backdrop:#e4e4e4;
  }
  *{box-sizing:border-box;margin:0;padding:0}
  html,body{width:1200px;height:900px;overflow:hidden}
  body{background:var(--backdrop);font-family:'Raleway',sans-serif;color:var(--ink);position:relative}

  .page{position:absolute;top:54px;width:560px;height:792px;background:var(--paper);overflow:hidden;box-shadow:0 6px 18px rgba(0,0,0,.18)}
  .page--back{left:25px}
  .page--front{left:615px}

  /* FRONT */
  .top-band{height:26px;background:var(--rose);border-bottom:3px solid var(--sage-line)}
  .brand{position:absolute;left:46px;top:72px;display:flex;align-items:center;gap:10px;color:var(--rose);font-weight:300;font-size:15px}
  .brand__dot{width:14px;height:14px;border-radius:50%;background:var(--rose-soft)}
  .rule{position:absolute;left:46px;height:1px;background:var(--sage-line)}
  .headline{position:absolute;left:46px;top:160px;font-size:52px;line-height:1.02;font-weight:400;color:var(--rose);letter-spacing:.5px}
  .headline strong{font-weight:800;color:var(--sage)}
  .intro{position:absolute;left:46px;top:290px;width:450px;font-size:12.2px;line-height:1.45;color:var(--ink)}
  .intro em{font-weight:700}
  .front-photo{position:absolute;left:0;top:390px;width:560px;height:402px;background:radial-gradient(ellipse at 45% 55%,#f3dccd 0%,#e9cdbb 35%,#f4efec 70%,#fafafa 100%)}
  .front-footer{position:absolute;left:0;bottom:22px;width:560px;display:flex;align-items:center;gap:14px;padding:0 0 0 0}
  .front-footer__line{height:1px;background:var(--sage-line);flex:1}
  .front-footer__url{font-size:11.5px;letter-spacing:3.2px;color:#8a8a8a;font-weight:400}

  /* BACK */
  .back-photo{position:absolute;inset:0;background:linear-gradient(160deg,#f8efeb 0%,#f2ddd5 40%,#f7ebe6 70%,#fbf6f3 100%)}
  .back-content{position:absolute;inset:0;padding:34px 34px 0 34px;font-size:10.6px;line-height:1.42}
  .lead{font-style:italic;margin-bottom:12px}
  .offer-band{background:var(--rose);color:#fff;font-size:16px;font-weight:400;padding:8px 14px;margin:0 -34px 10px;padding-left:34px}
  .offer-band strong{font-weight:800}
  .back-content p{margin-bottom:10px}
  .section-title{font-size:13px;font-weight:800;margin:4px 0 3px}
  .checklist{list-style:none;margin-bottom:10px}
  .checklist li{display:flex;gap:6px;align-items:flex-start}
  .checklist svg{flex:none;margin-top:2px}
  .contact-band{position:absolute;left:0;right:0;bottom:40px;background:var(--rose);color:#fff;display:flex;align-items:center;padding:12px 34px;gap:18px}
  .contact-band__name{font-size:21px;font-weight:500;letter-spacing:.5px;padding-right:18px;border-right:1px solid rgba(255,255,255,.7)}
  .contact-band__list{list-style:none;font-size:12px;font-weight:700;line-height:1.6}
  .contact-band__list li{display:flex;align-items:center;gap:7px}
  .footnote{position:absolute;left:34px;bottom:18px;font-size:9.5px;font-style:italic;color:#777}
</style>
</head>
<body>

<section class="page page--back" aria-label="Flyer back">
  <div class="back-photo" role="img" aria-label="Soft faded photo of a parent cuddling a sleeping baby"></div>
  <div class="back-content">
    <p class="lead">Of course nobody plans to have a sleep problem, but habits can become easily ingrained and spiral quickly out of control and you can find yourself sleep deprived, desperate and not too sure what to do. You see all the other sleeping babies and wish there was someone who understood what you were going through?! Well, there is!</p>
    <div class="offer-band">Contact me for a free <strong>15 minute</strong> consultation</div>
    <p>This 15 minute “mini” consultation is a chance to discuss your unique sleep challenges and sleep goals with me. I will provide you with an overview of how I will work with your family to achieve your wildest sleep dreams. I understand and believe that every child and their family is unique and there is no one size fits all! I would love to have a chat with you and talk about how I can help make things easier for you and your family!</p>

    <h2 class="section-title">Do I need a sleep consultant for my child?</h2>
    <p style="margin-bottom:2px">The answer is yes if:</p>
    <ul class="checklist">
      <li><svg width="9" height="9" viewBox="0 0 10 10"><circle cx="5" cy="5" r="4" fill="none" stroke="#3a3a3a" stroke-width="1.2"/></svg>your child will only fall asleep when nursing or bottle feeding</li>
      <li><svg width="9" height="9" viewBox="0 0 10 10"><circle cx="5" cy="5" r="4" fill="none" stroke="#3a3a3a" stroke-width="1.2"/></svg>your child needs a dummy or other external aid, like being rocked, patted or taken for a car ride to fall asleep</li>
      <li><svg width="9" height="9" viewBox="0 0 10 10"><circle cx="5" cy="5" r="4" fill="none" stroke="#3a3a3a" stroke-width="1.2"/></svg>your good night routine is a challenging and exhausting procedure instead of a relaxed and enjoyable moment for the whole family</li>
      <li><svg width="9" height="9" viewBox="0 0 10 10"><circle cx="5" cy="5" r="4" fill="none" stroke="#3a3a3a" stroke-width="1.2"/></svg>sleep is a constant battle in your home which leaves you feeling frustrated and exhausted</li>
      <li><svg width="9" height="9" viewBox="0 0 10 10"><circle cx="5" cy="5" r="4" fill="none" stroke="#3a3a3a" stroke-width="1.2"/></svg>your own lack of sleep is taking a toll on you and the whole family</li>
    </ul>

    <h2 class="section-title">What can I do for you?</h2>
    <p style="margin-bottom:2px">I will:</p>
    <ul class="checklist">
      <li><svg width="9" height="9" viewBox="0 0 10 10"><circle cx="5" cy="5" r="4" fill="none" stroke="#3a3a3a" stroke-width="1.2"/></svg>Guide you to set an age appropriate foundation for good sleep</li>
      <li><svg width="9" height="9" viewBox="0 0 10 10"><circle cx="5" cy="5" r="4" fill="none" stroke="#3a3a3a" stroke-width="1.2"/></svg>Create an individual sleep plan tailored especially to your child’s sleep needs and circumstances</li>
      <li><svg width="9" height="9" viewBox="0 0 10 10"><circle cx="5" cy="5" r="4" fill="none" stroke="#3a3a3a" stroke-width="1.2"/></svg>Help you to teach your child to go to sleep and get back to sleep independently during the night</li>
      <li><svg width="9" height="9" viewBox="0 0 10 10"><circle cx="5" cy="5" r="4" fill="none" stroke="#3a3a3a" stroke-width="1.2"/></svg>Show you how to teach your child to take healthful, restorative naps</li>
      <li><svg width="9" height="9" viewBox="0 0 10 10"><circle cx="5" cy="5" r="4" fill="none" stroke="#3a3a3a" stroke-width="1.2"/></svg>Learn</li>
    </ul>
  </div>

  <div class="contact-band">
    <div class="contact-band__name">Marta Lindqvist</div>
    <ul class="contact-band__list">
      <li><svg width="12" height="12" viewBox="0 0 12 12"><circle cx="6" cy="6" r="5.3" fill="none" stroke="#fff"/><path d="M4 3.5l1 1-0.6 .8a4 4 0 0 0 2.3 2.3l.8-.6 1 1-.8.9C5.6 8.7 3.3 6.4 3.1 4.3z" fill="#fff"/></svg>+34 612 380 574</li>
      <li><svg width="12" height="12" viewBox="0 0 12 12"><circle cx="6" cy="6" r="5.3" fill="none" stroke="#fff"/><rect x="3.2" y="4" width="5.6" height="4" fill="none" stroke="#fff" stroke-width=".9"/><path d="M3.2 4l2.8 2.2L8.8 4" fill="none" stroke="#fff" stroke-width=".9"/></svg>info@quietmeadowstudio-example.com</li>
      <li><svg width="12" height="12" viewBox="0 0 12 12"><circle cx="6" cy="6" r="5.3" fill="none" stroke="#fff"/><circle cx="6" cy="6" r="3" fill="none" stroke="#fff" stroke-width=".9"/><path d="M3 6h6M6 3v6" stroke="#fff" stroke-width=".8"/></svg>www.quietmeadowstudio-example.com</li>
    </ul>
  </div>
  <p class="footnote">*Consultations in English, German or Spanish via Phone/VidLink or home consultation</p>
</section>

<section class="page page--front" aria-label="Flyer front">
  <div class="top-band"></div>
  <div class="brand"><span class="brand__dot"></span><span>The Quiet Meadow Studio</span></div>
  <div class="rule" style="top:128px;width:210px"></div>
  <h1 class="headline">IS <strong>SLEEP</strong> AN ISSUE<br>IN <strong>YOUR HOME?</strong></h1>
  <div class="rule" style="top:272px;width:468px"></div>
  <p class="intro"><em>The Quiet Meadow Studio</em> is a pediatric sleep consultancy that specializes in helping parents with children who struggle to develop good and healthy sleep habits. Disruptive sleep patterns or not enough sleep can affect the physical, mental and emotional development of your child.</p>
  <div class="rule" style="top:368px;width:278px"></div>
  <div class="front-photo" role="img" aria-label="Photo of a toddler sleeping peacefully on a white pillow"></div>
  <div class="front-footer">
    <span class="front-footer__line" style="flex:0 0 120px"></span>
    <span class="front-footer__url">www.quietmeadowstudio-example.com</span>
    <span class="front-footer__line"></span>
  </div>
</section>

</body>
</html>
```